Educational clinic needs a new webpage design

I have a relatively new website but I am unhappy with the design. I was hoping the look of it would more match my logo, brochures, business cards, and postcards. The content is good and it's already mobile ready. The designer used square space, which I would like to keep if possible. My website is www.harborlightstudyhouse.example

Target Market(s)

Parents of school age children

Industry/Entity Type

Education

Number of Pages Required

5+ page

Requirements
Must have
• Pictures must depict the diversity of our students. We service all ages, from preschool through college and our students come from varying races.
Should not have
• I try to avoid the word "tutoring" because what we do is so much more. I like the tag line of "results that go beyond traditional tutoring"

```html
<!DOCTYPE html>
<html lang="en">
<head>
<meta charset="utf-8">
<title>Harbor Light Study House</title>
<link href="https://fonts.googleapis.com/css2?family=Arimo:wght@400;700&family=Playfair+Display:ital,wght@1,400&display=swap" rel="stylesheet">
<style>
:root{
  --purple:#5c2d84;
  --purple-light:#9b5cc6;
  --purple-deep:#4a2170;
  --green:#8cc63f;
  --green-dark:#3f5e16;
  --chalk:#2e2e2e;
  --paper:#f1f1ef;
  --ink:#1e1e1e;
  --footer:#2b2b2b;
  --blue:#1a7fc4;
  --white:#ffffff;
}
*{box-sizing:border-box;margin:0;padding:0}
html,body{width:741px;height:1200px;overflow:hidden}
body{font-family:"Arimo",Arial,sans-serif;background:var(--paper);color:var(--ink);position:relative}
.site-header{position:absolute;top:0;left:0;width:741px;height:48px;background:var(--purple);display:flex;align-items:center;justify-content:space-between;padding:0 45px 0 55px}
.brand{display:flex;align-items:center;gap:8px;color:var(--white)}
.brand-mark{width:26px;height:26px;border-radius:50%;background:var(--white)}
.brand-name{font-weight:700;font-size:12px;line-height:12px;letter-spacing:.5px}
.brand-name span{display:block;font-weight:700;font-size:9px;letter-spacing:1.5px}
.main-nav{display:flex;gap:13px}
.main-nav a{color:var(--white);text-decoration:none;font-size:11px}
.hero{position:absolute;top:48px;left:0;width:741px;height:282px;background:radial-gradient(ellipse at 50% 50%,#3a3a3a 0%,var(--chalk) 60%,#1f1f1f 100%)}
.hero-title{position:absolute;left:84px;top:76px;font-family:"Playfair Display",Georgia,serif;font-style:italic;font-size:45px;line-height:58px}
.hero-title .line-one{color:var(--purple-light);display:block}
.hero-title .line-two{color:var(--green);display:block}
.hero-art{position:absolute;left:455px;top:56px;width:195px;height:206px;border-radius:50% 50% 40% 40%;background:linear-gradient(180deg,var(--purple-light) 0%,var(--purple-light) 58%,var(--green) 62%,#6f9e2e 100%);opacity:.85}
.intro{position:absolute;top:330px;left:152px;width:460px}
.intro h1{font-size:18px;font-weight:700;margin-top:40px;margin-bottom:10px}
.intro p{font-size:11px;line-height:14px;margin-bottom:13px}
.btn-outline{position:absolute;left:1px;top:181px;width:112px;height:30px;border:2px solid var(--purple-light);border-radius:13px;color:var(--purple-light);font-weight:700;font-size:11px;display:flex;align-items:center;justify-content:center}
.feature{position:absolute;top:602px;left:0;width:741px;height:283px;background:linear-gradient(160deg,#8a5aa8 0%,var(--purple) 55%,var(--purple-deep) 100%);overflow:hidden}
.feature-photo{position:absolute;left:0;top:0;width:370px;height:283px;background:linear-gradient(135deg,#e9e6ea 0%,#c9b7d8 35%,#8cc63f 55%,#5c2d84 75%,#e4a35c 100%)}
.feature-copy{position:absolute;left:386px;top:66px;width:250px;color:var(--white)}
.feature-copy h2{font-size:17px;font-weight:700;margin-bottom:12px}
.feature-copy p{font-size:11px;line-height:13.5px;margin-bottom:13px}
.btn-green{position:absolute;left:-2px;top:126px;width:161px;height:30px;background:var(--green);border-radius:9px;color:var(--green-dark);font-weight:700;font-size:11px;display:flex;align-items:center;justify-content:center}
.subscribe{position:absolute;top:952px;left:148px;width:430px}
.subscribe p{font-size:11px;margin-left:4px;margin-bottom:10px}
.subscribe-form{display:flex}
.subscribe-input{width:325px;height:29px;background:var(--white);border:1px solid #d8d8d8;border-radius:9px 0 0 9px;font-size:11px;color:#666;display:flex;align-items:center;padding-left:13px}
.subscribe-button{width:102px;height:29px;border:2px solid var(--blue);border-radius:0 9px 9px 0;background:var(--white);color:var(--blue);font-weight:700;font-size:11px;display:flex;align-items:center;justify-content:center}
.site-footer{position:absolute;top:1088px;left:0;width:741px;height:112px;background:var(--footer);color:var(--white);font-size:9.5px;line-height:11.8px}
.footer-col{position:absolute;top:28px;display:flex;flex-direction:column}
.footer-col a{color:var(--white)}
.footer-col strong{font-weight:700}
.col-programs{left:62px}
.col-about{left:188px}
.footer-contact{position:absolute;top:28px;right:106px;text-align:right}
.footer-contact a{color:var(--white)}
.social-square{position:absolute;top:31px;right:29px;width:28px;height:28px;background:var(--white)}
</style>
</head>
<body>
<header class="site-header">
  <div class="brand">
    <div class="brand-mark"></div>
    <div class="brand-name">HARBOR LIGHT<span>Study House</span></div>
  </div>
  <nav class="main-nav">
    <a href="#">Our Programs</a><a href="#">About</a><a href="#">FAQs</a><a href="#">Payments</a><a href="#">Contact</a>
  </nav>
</header>

<section class="hero">
  <h1 class="hero-title"><span class="line-one">Nurturing Minds</span><span class="line-two">of All Kinds</span></h1>
  <div class="hero-art" role="img" aria-label="Chalk drawing of a purple brain held by two green hands"></div>
</section>

<section class="intro">
  <h1>Learning programs your child deserves.</h1>
  <p>Is school a struggle? Are you and your child spending twice as much time doing homework as you should be? Are you frustrated and at your wits end? Have you been told your child has a learning disability? Do you hear things like, "your child is lazy," or "he can't focus or attend."</p>
  <p>We want to see the children of tomorrow succeed.We want to work with you and your child to address their needs to strive for the best results.</p>
  <div class="btn-outline">Learn More</div>
</section>

<section class="feature">
  <div class="feature-photo" role="img" aria-label="Photo of a diverse group of cheering schoolchildren with backpacks, arms raised, over purple and green stripes"></div>
  <div class="feature-copy">
    <h2>Life-Changing Learning</h2>
    <p>We want our students to become self-sufficient, independent learners. Get results that go beyond traditional tutoring.</p>
    <p>First-time clients get a FREE consultation.</p>
    <div class="btn-green">Request Consultation</div>
  </div>
</section>

<section class="subscribe">
  <p>Subscribe by e-mail to keep updated on the latest news.</p>
  <div class="subscribe-form">
    <div class="subscribe-input">address@email.com</div>
    <div class="subscribe-button">Subscribe</div>
  </div>
</section>

<footer class="site-footer">
  <div class="footer-col col-programs">
    <strong>Our Programs</strong>
    <a href="#">How We Can Help</a>
    <a href="#">Exam Prep</a>
    <a href="#">Specialty Programs</a>
    <a href="#">Summer Sessions</a>
  </div>
  <div class="footer-col col-about">
    <a href="#">About</a>
    <a href="#">FAQs</a>
    <a href="#">Payments</a>
    <a href="#">Contact</a>
  </div>
  <div class="footer-contact">
    Harbor Light Study House<br>
    418 Lantern Row, Bayview, IL, 60990<br>
    Call&nbsp; 555-014-2870<br>
    Email&nbsp; <a href="#">info@harborlightstudyhouse.example</a>
  </div>
  <div class="social-square"></div>
</footer>
</body>
</html>
```